Brisket Dwelling Review is a leading provider of residential appraisal and home inspection products in S

I need a business card/logo designed that obviously describes my business. We are a residential appraisal and home inspection company in Springfield, MO. We offer residential appraisals, home inspection, pest inspection and radon gas measurement. We have been in business for 18 years and hold state certified residential appraisal licenses and VORMEL certified home inspection licenses. I have a logo that I really like and will attach, but would be open to new suggestions. I like more modern designs than traditional and would like a two sided card with our services, licenses and qualifications on the back.

```html
<!DOCTYPE html>
<html lang="en">
<head>
<meta charset="utf-8">
<title>Brisket Dwelling Review – Business Card</title>
<link rel="stylesheet" href="https://fonts.googleapis.com/css2?family=Open+Sans:wght@400;600;700&display=swap">
<style>
  :root {
    --bg: #e9e6e0;
    --paper: #ffffff;
    --gold: #ac8f58;
    --gold-dark: #9c8049;
    --gold-light: #c2a775;
    --amber: #f0b323;
    --name-gold: #b3965f;
    --title-amber: #e8a92a;
    --ink-light: #fbf7ef;
  }
  * { box-sizing: border-box; margin: 0; padding: 0; }
  html, body { width: 1200px; height: 780px; overflow: hidden; }
  body {
    background: var(--bg);
    font-family: "Open Sans", Arial, sans-serif;
    display: flex;
    align-items: center;
    justify-content: center;
    gap: 40px;
  }
  .card {
    position: relative;
    width: 550px;
    height: 314px;
    overflow: hidden;
    box-shadow: 0 6px 18px rgba(0,0,0,0.18);
  }

  /* Front */
  .card-front { background: var(--paper); }
  .front-swoosh { position: absolute; inset: 0; width: 100%; height: 100%; }
  .brand-front {
    position: absolute;
    left: 40px;
    top: 128px;
    display: flex;
    align-items: center;
    gap: 10px;
  }
  .brand-mark {
    width: 14px; height: 14px;
    flex: none;
    background: var(--amber);
  }
  .brand-name {
    font-weight: 700;
    font-size: 21px;
    line-height: 1.1;
    color: var(--gold);
    width: 190px;
  }
  .employee {
    position: absolute;
    right: 210px;
    top: 24px;
    text-align: right;
  }
  .employee-name {
    font-size: 20px;
    font-weight: 600;
    line-height: 1.2;
    color: var(--name-gold);
  }
  .employee-title {
    font-size: 13px;
    line-height: 1.3;
    color: var(--title-amber);
  }
  .contact {
    position: absolute;
    right: 22px;
    top: 150px;
    list-style: none;
    text-align: right;
    color: var(--ink-light);
    font-size: 12px;
    line-height: 22px;
  }
  .contact li { display: flex; justify-content: flex-end; align-items: center; gap: 8px; }
  .contact svg { width: 11px; height: 11px; fill: var(--ink-light); flex: none; }

  /* Back */
  .card-back {
    background: linear-gradient(150deg, var(--gold-light) 0%, var(--gold) 45%, var(--gold-dark) 100%);
    color: var(--ink-light);
  }
  .brand-back {
    position: absolute;
    left: 34px;
    top: 30px;
    display: flex;
    align-items: center;
    gap: 10px;
  }
  .brand-back .brand-mark { background: var(--ink-light); }
  .brand-back .brand-name { color: var(--ink-light); width: auto; font-size: 22px; }
  .brand-rule {
    position: absolute;
    left: 34px; top: 66px;
    width: 250px; height: 1px;
    background: var(--ink-light);
  }
  .about {
    position: absolute;
    left: 34px; top: 86px;
    width: 470px;
    font-size: 13px;
    line-height: 19px;
  }
  .services {
    position: absolute;
    left: 34px; top: 178px;
  }
  .services h2 {
    font-size: 15px;
    font-weight: 700;
    letter-spacing: 0.5px;
    margin-bottom: 6px;
  }
  .services p { font-size: 13px; line-height: 20px; }
  .social {
    position: absolute;
    right: 30px; bottom: 26px;
    display: flex; gap: 8px;
  }
  .social span {
    width: 22px; height: 22px;
    border-radius: 3px;
    background: var(--ink-light);
    opacity: 0.85;
  }
</style>
</head>
<body>

  <section class="card card-front">
    <svg class="front-swoosh" viewBox="0 0 550 314" aria-hidden="true">
      <path d="M430 0 C300 90 300 220 170 314 L550 314 L550 0 Z" fill="var(--gold)"/>
      <path d="M320 110 C290 210 250 270 115 314 L150 314 C270 262 305 200 320 110 Z" fill="var(--amber)"/>
      <path d="M300 250 C270 280 240 300 200 314 L214 314 C250 300 280 282 300 262 Z" fill="#ffffff" opacity="0.85"/>
    </svg>

    <div class="brand-front">
      <span class="brand-mark"></span>
      <span class="brand-name">Brisket Dwelling Review</span>
    </div>

    <div class="employee">
      <p class="employee-name">Employee Name</p>
      <p class="employee-title">Managing Director</p>
    </div>

    <ul class="contact">
      <li>000.000.0000
        <svg viewBox="0 0 12 12"><path d="M2 1h3l1 3-2 1a7 7 0 0 0 3 3l1-2 3 1v3c-6 0-9-4-9-9z"/></svg></li>
      <li>review@youremail.com
        <svg viewBox="0 0 12 12"><path d="M0 2h12v8H0z M1 3l5 4 5-4" stroke="#ac8f58" stroke-width="1"/></svg></li>
      <li>www.yourwebsite.com
        <svg viewBox="0 0 12 12"><circle cx="6" cy="6" r="5.5"/></svg></li>
      <li>000 Larkfield Rd, Ashbury, USA
        <svg viewBox="0 0 12 12"><path d="M6 0a4 4 0 0 1 4 4c0 3-4 8-4 8S2 7 2 4a4 4 0 0 1 4-4z"/></svg></li>
    </ul>
  </section>

  <section class="card card-back">
    <div class="brand-back">
      <span class="brand-mark"></span>
      <span class="brand-name">Brisket Dwelling Review</span>
    </div>
    <div class="brand-rule"></div>

    <p class="about">We have been in business for 18 years and hold state certified residential appraisal licenses and VORMEL certified home inspection licenses</p>

    <div class="services">
      <h2>OUR SERVICES</h2>
      <p>residential appraisals / home inspection</p>
      <p>pest inspection / radon gas measurement</p>
    </div>

    <div class="social" aria-hidden="true">
      <span></span><span></span><span></span>
    </div>
  </section>

</body>
</html>
```